Printing company needs website!

A printing company would like a new professional website (made with wix). Now they don't have a website, but they want a unique, beautiful, clear site. Of course they provide the content themselves, we are now looking for the beautiful design with some mockups. You can see several of their projects on their instagram & facebook.
Www.pagenook.com/velmoor and https://www.snapfolio.com/velmoor.be/ logos are attached.

```html
<!DOCTYPE html>
<html lang="en">
<head>
<meta charset="utf-8">
<title>Velmoor – Best Printing Services</title>
<link href="https://fonts.googleapis.com/css2?family=Poppins:wght@300;400;500;600;700;800&display=swap" rel="stylesheet">
<style>
:root{
  --teal:#3bbfad;
  --teal-dark:#2aa796;
  --yellow:#fbd005;
  --blue:#1ca5dc;
  --ink:#222b33;
  --text:#555d66;
  --footer:#12353d;
  --white:#ffffff;
}
*{margin:0;padding:0;box-sizing:border-box}
html,body{width:1200px;height:4289px;overflow:hidden}
body{position:relative;font-family:'Poppins',sans-serif;color:var(--ink);background:var(--white)}
.abs{position:absolute}
.photo{position:absolute}

/* header */
.header{position:absolute;left:0;top:0;width:1200px;height:80px;background:var(--white);border-bottom:1px solid #eee}
.brand{position:absolute;display:flex;align-items:center;gap:10px}
.brand-dot{width:40px;height:40px;border-radius:50%;background:var(--teal)}
.brand-name{font-weight:600;font-size:32px;color:var(--ink);line-height:1}
.brand-tag{font-size:9px;color:var(--teal);display:block;margin-top:3px;font-weight:400}
.nav a{position:absolute;top:32px;font-size:15px;color:var(--ink);text-decoration:none}
.nav a.active{color:var(--teal);border-bottom:2px solid var(--teal);padding-bottom:6px}
.header-phone{position:absolute;left:948px;top:28px;display:flex;align-items:center;gap:10px;font-weight:600;font-size:16px}
.phone-ico{width:26px;height:26px;border-radius:50%;background:var(--teal);display:flex;align-items:center;justify-content:center}

/* hero */
.hero{position:absolute;left:0;top:80px;width:1200px;height:574px;background:linear-gradient(160deg,#5b636b,#8d9094 45%,#c9c6bd 70%,#6f7479);}
.hero-shade{position:absolute;inset:0;background:rgba(20,25,30,.35)}
.hero-kicker{position:absolute;top:172px;width:100%;text-align:center;color:#fff;font-weight:300;font-size:29px}
.hero-title{position:absolute;top:208px;width:100%;text-align:center;color:#fff;font-weight:700;font-size:54px}
.btn{position:absolute;display:flex;align-items:center;justify-content:center;border-radius:30px;font-weight:600;font-size:16px;text-transform:uppercase;color:#fff;background:var(--teal)}
.arrow{position:absolute;top:300px}

/* circles */
.circle{position:absolute;width:300px;height:300px;border-radius:50%;display:flex;align-items:center;justify-content:center}
.circle-inner{width:252px;height:252px;border-radius:50%;display:flex;flex-direction:column;align-items:center;justify-content:center;text-align:center;color:#fff;padding:0 36px}
.circle-icon{width:72px;height:72px;border-radius:50%;background:rgba(255,255,255,.25);display:flex;align-items:center;justify-content:center;margin-bottom:14px}
.circle h3{font-weight:400;font-size:19px;margin-bottom:6px}
.circle h3 b{font-weight:700}
.circle p{font-size:11px;line-height:1.35}

/* section heads */
.kicker{position:absolute;width:100%;text-align:center;color:var(--teal);font-size:22px;font-weight:400}
.sec-title{position:absolute;width:100%;text-align:center;font-size:42px;font-weight:400;color:var(--ink)}
.sec-title b{font-weight:700}

.services-bg{position:absolute;left:0;top:850px;width:1200px;height:640px;background-image:linear-gradient(#eef3f6 1px,transparent 1px),linear-gradient(90deg,#eef3f6 1px,transparent 1px);background-size:22px 22px}
.lead{position:absolute;left:220px;width:760px;text-align:center;font-size:17px;line-height:1.6;color:var(--text)}
.service-tile{position:absolute;top:1168px;width:243px;height:210px}
.service-tile span{position:absolute;left:18px;bottom:12px;color:#fff;font-weight:700;font-size:16px;text-transform:uppercase}
.btn-outline{position:absolute;left:493px;top:1411px;width:221px;height:53px;border:2px solid var(--teal);border-radius:30px;color:var(--teal);font-weight:600;font-size:15px;display:flex;align-items:center;justify-content:center;background:#fff}

/* about */
.about-photo{left:0;top:1553px;width:536px;height:527px;border-radius:0 270px 270px 0 / 0 264px 264px 0;background:linear-gradient(120deg,#b9b6b1,#6d6a66 50%,#3d3b42)}
.about-kicker{position:absolute;left:614px;top:1612px;color:var(--yellow);font-size:22px}
.about-title{position:absolute;left:614px;top:1640px;font-size:48px;font-weight:400}
.about-title b{color:var(--teal);font-weight:700}
.about-text{position:absolute;left:616px;width:480px;font-size:16px;line-height:1.7;color:var(--text)}

/* why */
.why{position:absolute;left:0;top:2080px;width:1200px;height:644px;background:var(--yellow)}
.why-title{position:absolute;top:2200px;width:100%;text-align:center;color:#fff;font-size:34px;font-weight:400}
.why-title b{font-weight:700}
.why-rule{position:absolute;left:580px;top:2256px;width:56px;height:3px;background:#fff}
.feature{position:absolute;left:135px;display:flex;gap:18px;align-items:flex-start}
.feature-ico{width:80px;height:80px;border-radius:50%;background:#fff;flex:none;display:flex;align-items:center;justify-content:center}
.feature h4{color:#fff;font-weight:700;font-size:17px;text-transform:uppercase;margin-top:10px}
.feature p{color:#fff;font-size:13px;line-height:1.6;width:320px}
.why-photo{left:624px;top:2305px;width:456px;height:342px;border-radius:40px 0 0 40px / 40px 0 0 40px;background:linear-gradient(160deg,#4a4f56,#2a2e33 45%,#c34c7e 70%,#2c74c4)}
.dots{position:absolute;background-image:radial-gradient(#fff 1.6px,transparent 1.7px);background-size:14px 14px}

/* gallery */
.gal-rule{position:absolute;left:564px;top:2849px;width:72px;height:4px;background:var(--teal)}
.dots-grey{position:absolute;background-image:radial-gradient(#9fc8d8 1.6px,transparent 1.7px);background-size:14px 14px}
.card{position:absolute;width:290px;height:292px;background:#fff;box-shadow:0 4px 20px rgba(0,0,0,.08);text-align:center;padding-top:38px}
.card h5{font-size:18px;font-weight:600;color:#444;text-transform:uppercase}
.card p{font-size:12px;color:#888;margin-top:2px}
.card .photo{left:30px;right:30px;bottom:24px;height:160px}
.card.featured{background:var(--teal)}
.card.featured h5,.card.featured p{color:#fff}

/* contact */
.contact{position:absolute;left:0;top:3336px;width:1200px;height:566px;background:linear-gradient(90deg,#46c1a8,#2ab6c4)}
.contact-photo{left:640px;top:3336px;width:560px;height:566px;border-radius:280px 0 0 280px / 283px 0 0 283px;background:linear-gradient(135deg,#2b2f35,#6a5b55 40%,#b3452f 60%,#2d3238)}
.c-kicker{position:absolute;left:123px;top:3440px;color:#fff;font-size:20px}
.c-title{position:absolute;left:123px;top:3464px;color:#fff;font-size:38px;font-weight:400;border-bottom:3px solid #fff;line-height:1.25}
.c-title b{font-weight:700}
.field{position:absolute;background:#fff;border:1px solid #d8e6e6;font-size:12px;color:#555;padding:14px 16px}
.btn-yellow{background:var(--yellow);color:#fff;font-size:14px}

/* footer */
.footer{position:absolute;left:0;top:3902px;width:1200px;height:387px;background:var(--footer);color:#d8e3e5}
.foot-col{position:absolute;top:70px;border-left:2px solid #1f4952;padding-left:18px;height:140px}
.foot-col h6{font-size:15px;font-weight:700;color:#fff;text-transform:uppercase;margin-bottom:16px;position:relative}
.foot-col h6::before{content:"";position:absolute;left:-20px;top:0;width:2px;height:20px;background:var(--yellow)}
.foot-col a{display:block;font-size:12px;color:#d8e3e5;text-decoration:none;margin-bottom:12px}
.contact-item{display:flex;gap:14px;align-items:flex-start;margin-bottom:14px;font-size:11px}
.contact-item strong{display:block;font-size:15px;font-weight:400;color:#fff}
.contact-item .v{display:block;font-size:12px;color:#fff}
.foot-about{position:absolute;left:143px;top:168px;width:250px;font-size:11px;line-height:1.8;color:#8fa8ad}
.copyright{position:absolute;left:0;top:4215px;width:100%;border-top:1px solid #1f4952;text-align:center;padding-top:30px;font-size:12px;color:#8fa8ad}
</style>
</head>
<body>

<header class="header">
  <div class="brand" style="left:92px;top:16px">
    <span class="brand-dot"></span>
    <span class="brand-name">Velmoor<span class="brand-tag">waar alles velmoor is</span></span>
  </div>
  <nav class="nav">
    <a class="active" style="left:363px" href="#">About Us</a>
    <a style="left:474px" href="#">Our Services</a>
    <a style="left:612px" href="#">Printing</a>
    <a style="left:714px" href="#">Our Work</a>
    <a style="left:829px" href="#">Contact Us</a>
  </nav>
  <div class="header-phone">
    <span class="phone-ico"><svg width="14" height="14" viewBox="0 0 24 24"><path fill="#fff" d="M6.6 10.8a15 15 0 0 0 6.6 6.6l2.2-2.2c.3-.3.7-.4 1-.2 1.1.4 2.3.6 3.6.6.6 0 1 .4 1 1V20c0 .6-.4 1-1 1A17 17 0 0 1 3 4c0-.6.4-1 1-1h3.5c.6 0 1 .4 1 1 0 1.3.2 2.5.6 3.6.1.3 0 .7-.2 1z"/></svg></span>
    0470 1123 45
  </div>
</header>

<section class="hero" role="img" aria-label="Printing press with printed sheets on the feed table">
  <div class="hero-shade"></div>
  <div class="hero-kicker">Welcome to Velmoor</div>
  <h1 class="hero-title">Best Printing Services</h1>
  <div class="btn" style="left:507px;top:294px;width:200px;height:52px">Request Quote</div>
  <svg class="arrow" style="left:34px" width="28" height="44" viewBox="0 0 28 44"><path d="M22 4 6 22l16 18" fill="none" stroke="#fff" stroke-width="5"/></svg>
  <svg class="arrow" style="left:1130px" width="28" height="44" viewBox="0 0 28 44"><path d="M6 4l16 18L6 40" fill="none" stroke="#fff" stroke-width="5"/></svg>
</section>

<div class="circle" style="left:133px;top:574px;background:rgba(28,165,220,.3)">
  <div class="circle-inner" style="background:var(--blue)">
    <div class="circle-icon"><svg width="34" height="34" viewBox="0 0 24 24" fill="none" stroke="#fff" stroke-width="1.5"><path d="M12 2 3 7v10l9 5 9-5V7z"/><path d="M3 7l9 5 9-5M12 12v10"/></svg></div>
    <h3>PRINTING <b>SERVICE</b></h3>
    <p>Lorem ipsum dolor sit amet, consectetur adipiscing elit, sed do eiusmo</p>
  </div>
</div>
<div class="circle" style="left:454px;top:574px;background:rgba(251,208,5,.35)">
  <div class="circle-inner" style="background:var(--yellow)">
    <div class="circle-icon"><svg width="34" height="34" viewBox="0 0 24 24" fill="none" stroke="#fff" stroke-width="1.5"><rect x="3" y="5" width="8" height="14"/><rect x="13" y="3" width="8" height="14"/><path d="M5 9h4M5 12h4M15 7h4M15 10h4"/></svg></div>
    <h3>OUR <b>WORK</b></h3>
    <p>Lorem ipsum dolor sit amet, consectetur adipiscing elit, sed do eiusmo</p>
  </div>
</div>
<div class="circle" style="left:770px;top:574px;background:rgba(59,191,173,.35)">
  <div class="circle-inner" style="background:var(--teal)">
    <div class="circle-icon"><svg width="34" height="34" viewBox="0 0 24 24" fill="none" stroke="#fff" stroke-width="1.5"><rect x="4" y="3" width="13" height="18"/><path d="M7 8h7M7 11h7M7 14h4M20 6l-6 8-1 3 3-1 6-8z"/></svg></div>
    <h3>REQUEST <b>QUOTE</b></h3>
    <p>Lorem ipsum dolor sit amet, consectetur adipiscing elit, sed do eiusmo</p>
  </div>
</div>

<div class="services-bg"></div>
<div class="abs" style="left:605px;top:910px;width:2px;height:63px;background:var(--teal)"></div>
<div class="kicker" style="top:975px">Who We Are</div>
<h2 class="sec-title" style="top:998px"><b>Printing</b> Services</h2>
<p class="lead" style="top:1068px">Lorem ipsum dolor sit amet, consectetur adipiscing elit, sed do eiusmod tempor incididunt ut labore et dolore magna aliqua. Ut enim ad minim veniam.</p>

<div class="service-tile photo" role="img" aria-label="Colour test card printing in a press" style="left:103px;background:linear-gradient(135deg,#3a3d42,#7a6e8a 50%,#d44a8b 75%,#f0c23a);border-bottom:4px solid var(--yellow)"><span>Card Printing</span></div>
<div class="service-tile photo" role="img" aria-label="Large poster printing on a roll" style="left:356px;background:linear-gradient(135deg,#2d3035,#6b5f63 50%,#9a3f3f 80%,#2a3a55)"><span>Poster Printing</span></div>
<div class="service-tile photo" role="img" aria-label="Brochure sheets running through rollers" style="left:607px;background:linear-gradient(135deg,#c9cbcc,#7e8386 45%,#3c8f7c 70%,#d98a3a)"><span>Brochure Printing</span></div>
<div class="service-tile photo" role="img" aria-label="Wide format printer producing product prints" style="left:860px;background:linear-gradient(135deg,#d8d9da,#8a8d90 40%,#e09a2a 70%,#3d7fd0)"><span>Product Printing</span></div>

<div class="btn-outline">VIEW ALL SERVICES</div>

<div class="photo about-photo" role="img" aria-label="Two print workers checking printed sheets"></div>
<div class="about-kicker">Who We Are</div>
<h2 class="about-title">About <b>Velmoor</b></h2>
<p class="about-text" style="top:1728px">Lorem ipsum dolor sit amet, consectetur adipiscing elit, sed do eiusmod tempor incididunt ut labore et dolore</p>
<p class="about-text" style="top:1796px">Ut enim ad minim veniam, quis nostrud exercitation ullamco laboris nisi ut aliquip ex ea commodo consequat. Duis aute irure dolor in reprehenderit in voluptate velit esse cillum dolore eu fugiat ab illo inventore veritatis et quasi</p>
<div class="btn" style="left:614px;top:1928px;width:180px;height:46px;font-size:14px">Learn More</div>

<section class="why"></section>
<svg class="abs" style="left:0;top:2078px" width="1200" height="100" viewBox="0 0 1200 100">
  <path d="M0 0 H1200 V2 Q600 180 0 2 Z" fill="#fff"/>
  <path d="M100 18 Q600 140 1100 18" fill="none" stroke="var(--teal)" stroke-width="4"/>
</svg>
<h2 class="why-title">Why Choose <b>Velmoor</b></h2>
<div class="why-rule"></div>

<div class="feature" style="top:2312px;left:141px">
  <div class="feature-ico"><svg width="40" height="40" viewBox="0 0 24 24" fill="none" stroke="var(--teal)" stroke-width="1.4"><circle cx="12" cy="9" r="6"/><circle cx="12" cy="9" r="3"/><path d="M8 14l-2 7 3-1 2 2 1-5M16 14l2 7-3-1-2 2-1-5"/></svg></div>
  <div><h4>Quality Printing</h4><p>Lorem ipsum dolor sit amet consectetur Lorem ipsum dolor sit amet consectetur</p></div>
</div>
<div class="feature" style="top:2418px;left:135px">
  <div class="feature-ico"><svg width="40" height="40" viewBox="0 0 24 24" fill="none" stroke="var(--yellow)" stroke-width="1.4"><rect x="5" y="3" width="14" height="18"/><path d="M8 7h8M8 11h8M8 15h8M3 6h2M3 12h2M3 18h2M19 6h2M19 12h2M19 18h2"/></svg></div>
  <div><h4>Flexible Pricing</h4><p>Lorem ipsum dolor sit amet consectetur Lorem ipsum dolor sit amet consectetur</p></div>
</div>
<div class="feature" style="top:2530px;left:135px">
  <div class="feature-ico"><svg width="40" height="40" viewBox="0 0 24 24" fill="none" stroke="var(--blue)" stroke-width="1.4"><path d="M5 3h9l4 4v14H5z"/><path d="M8 10h7M8 13h7M8 16h5M19 12l3-1M19 15l3 1"/></svg></div>
  <div><h4>Offset Printing</h4><p>Lorem ipsum dolor sit amet consectetur Lorem ipsum dolor sit amet consectetur</p></div>
</div>

<div class="dots" style="left:815px;top:2460px;width:290px;height:210px"></div>
<div class="photo why-photo" role="img" aria-label="Large format printer printing a colourful image"></div>

<div class="kicker" style="top:2770px;font-size:20px">Project Gallery</div>
<h2 class="sec-title" style="top:2795px;font-size:38px"><b>Our Printing</b> Work</h2>
<div class="gal-rule"></div>
<div class="dots-grey" style="left:135px;top:2860px;width:290px;height:210px"></div>
<div class="dots-grey" style="left:840px;top:3070px;width:270px;height:200px"></div>

<div class="card" style="left:168px;top:2890px">
  <h5>Stickers</h5><p>Amet consectetur adipiscing elit</p>
  <div class="photo" role="img" aria-label="Printed stickers on coffee packaging" style="background:linear-gradient(120deg,#e8dccb,#c49a6c 45%,#2c2a2b 75%,#e34b3c)"></div>
</div>
<div class="card featured" style="left:476px;top:2915px">
  <h5>Poster</h5><p>Amet consectetur adipiscing elit</p>
  <div class="photo" role="img" aria-label="Printed banner poster with a building" style="background:linear-gradient(120deg,#f2f2f2,#9aa7ae 45%,#5b7b46 75%,#c8d3d8);bottom:50px;height:130px"></div>
</div>
<div class="card" style="left:784px;top:2948px">
  <h5>Magzine</h5><p>Amet consectetur adipiscing elit</p>
  <div class="photo" role="img" aria-label="Printed magazine cover held in a hand" style="background:linear-gradient(120deg,#f4f6f8,#7aa0d8 45%,#234fa0 75%,#f2f2f2)"></div>
</div>

<section class="contact"></section>
<div class="photo contact-photo" role="img" aria-label="Close-up of a printing press running colourful sheets"></div>
<div class="c-kicker">Get in touch</div>
<h2 class="c-title"><b>Contact</b> Us</h2>
<div class="field" style="left:123px;top:3536px;width:228px;height:40px">First Name</div>
<div class="field" style="left:359px;top:3536px;width:228px;height:40px">Last Name</div>
<div class="field" style="left:123px;top:3583px;width:228px;height:41px">Phone Number</div>
<div class="field" style="left:359px;top:3583px;width:228px;height:41px">Email address</div>
<div class="field" style="left:123px;top:3634px;width:464px;height:77px;padding-top:10px">Message</div>
<div class="btn btn-yellow" style="left:120px;top:3728px;width:175px;height:43px">Send Enquiry</div>

<footer class="footer">
  <div class="brand" style="left:125px;top:70px">
    <span class="brand-dot" style="width:56px;height:56px"></span>
    <span class="brand-name" style="color:#fff;font-size:40px">Velmoor<span class="brand-tag" style="text-align:right">waar alles velmoor is</span></span>
  </div>
  <p class="foot-about" style="top:168px">Lorem ipsum dolor sit amet, consectetur adipiscing elit, sed do eiusmod tempor incididunt ut labore et.</p>

  <div class="foot-col" style="left:454px">
    <h6>Navigation</h6>
    <a href="#">About Us</a><a href="#">Printing Services</a><a href="#">Why We Are</a><a href="#">Testimonials</a>
  </div>
  <div class="foot-col" style="left:666px">
    <h6>Resources</h6>
    <a href="#">Our Work</a><a href="#">Blogs</a><a href="#">Contact Us</a><a href="#">Privacy Policy</a>
  </div>
  <div class="foot-col" style="left:880px;border-left:none">
    <h6>Contact Us</h6>
    <div class="contact-item"><svg width="18" height="18" viewBox="0 0 24 24"><path fill="none" stroke="var(--teal)" stroke-width="2" d="M6.6 10.8a15 15 0 0 0 6.6 6.6l2.2-2.2 4.6 1.4V20A17 17 0 0 1 3 4h3.5l1.4 4.6z"/></svg><span>Phone<strong>0470 1123 45</strong></span></div>
    <div class="contact-item"><svg width="18" height="18" viewBox="0 0 24 24" fill="none" stroke="var(--teal)" stroke-width="2"><circle cx="12" cy="12" r="9"/><path d="M3 12h18M12 3c3 3 3 15 0 18M12 3c-3 3-3 15 0 18"/></svg><span>Website<span class="v">www.velmoor.be</span></span></div>
    <div class="contact-item"><svg width="18" height="18" viewBox="0 0 24 24" fill="none" stroke="var(--teal)" stroke-width="2"><rect x="3" y="5" width="18" height="14"/><path d="M3 6l9 7 9-7"/></svg><span>Email<span class="v">info@velmoor.be</span></span></div>
  </div>
</footer>
<div class="copyright">Copyright © 2022 Velmoor All Right Reserved</div>

</body>
</html>
```